Web Design Project

To develop a web based Council Meeting Support system which includes 2 major components for each Council member:
1. Allow a council member to Vote on a motion during a council session
2. Allow a council member to flag notify the Chair their intention to speak on a motion
The application will have 3 separate interfaces:
Chair interface: Allows the Chair of the session to review voting and manage the speaker queue
Council interface: Allows each council member to vote on each motion and add flag their intention to speak for or against a motion
Admin interface: Allows administrators to initiate a session and import details on all meeting participants
We will begin by designing the Council Interface. (An example wireframe is attached) This council interface will give members the ability to request to speak, vote, view voting results and viewing the current motion number.
*** 4 Designs will be required overall. One for each interface and a login page ***
Needs to be designed so that it works well on an Tavlo or any tablet device.
Update: Looking for a brighter design, not a dark grey one. The blue colour from qarvel.example would be good.
- Request to Speak
Voting
Vote Results
Current Motion Number

```html
<!DOCTYPE html>
<html lang="en">
<head>
<meta charset="utf-8">
<title>Qarvel Engineers – Council Interface</title>
<link href="https://fonts.googleapis.com/css2?family=Arimo:wght@400;700&display=swap" rel="stylesheet">
<style>
  :root {
    --brand-blue: #3fa0c8;
    --brand-navy: #1f3f73;
    --text-dark: #2b2b2b;
    --text-muted: #6a6a6a;
    --rule: #e6e6e6;
    --for-bg: #e2fbdd;
    --against-bg: #fde1df;
    --abstain-bg: #f5f0f0;
    --tick-green: #3cb43c;
    --cross-red: #d9262b;
    --neutral-grey: #9a9a9a;
    --white: #ffffff;
  }
  * { box-sizing: border-box; margin: 0; padding: 0; }
  html, body { width: 727px; height: 1200px; overflow: hidden; background: var(--white); }
  body { font-family: "Arimo", Arial, sans-serif; color: var(--text-dark); position: relative; }

  .site-header { position: absolute; top: 0; left: 0; width: 727px; height: 89px; border-bottom: 2px solid var(--rule); }
  .brand { position: absolute; left: 39px; top: 26px; display: flex; align-items: center; gap: 10px; }
  .brand-mark { width: 26px; height: 26px; background: var(--brand-blue); }
  .brand-name { font-size: 21px; font-weight: 700; color: var(--brand-navy); }
  .main-nav { position: absolute; right: 34px; top: 34px; display: flex; gap: 30px; font-size: 12px; font-weight: 700; }
  .main-nav a { color: var(--text-dark); text-decoration: none; }
  .main-nav a::after { content: " ›"; color: var(--neutral-grey); font-weight: 400; }

  .motion-band { position: absolute; top: 92px; left: 0; width: 727px; height: 93px; background: var(--brand-blue); color: var(--white); padding: 26px 36px 0; box-shadow: inset 0 6px 8px -4px rgba(0,0,0,.25); }
  .motion-title { font-size: 18px; font-weight: 700; }
  .motion-desc { font-size: 12px; margin-top: 6px; }

  .section-title { position: absolute; left: 36px; width: 655px; font-size: 13px; font-weight: 700; padding-bottom: 11px; border-bottom: 1px solid var(--rule); }
  .speak-title { top: 222px; }
  .results-title { top: 366px; }

  .speak-options { position: absolute; top: 286px; left: 36px; display: flex; }
  .speak-option { display: flex; align-items: center; gap: 12px; width: 214px; }
  .speak-option svg { width: 44px; height: 44px; flex: none; }
  .option-label { font-size: 14px; font-weight: 700; }
  .option-label.is-active { color: var(--brand-blue); }
  .option-sub { font-size: 8px; color: var(--text-muted); margin-top: 4px; text-transform: uppercase; }

  .result-column { position: absolute; top: 404px; width: 213px; padding: 8px 22px 0; }
  .result-column h3 { font-size: 11px; font-weight: 700; display: flex; align-items: center; gap: 10px; }
  .result-column h3::after { content: ""; flex: 1; height: 4px; background: rgba(0,0,0,.08); border-radius: 2px; }
  .result-column ul { list-style: none; margin-top: 14px; padding-left: 4px; }
  .result-column li { font-size: 10px; color: var(--text-muted); line-height: 16.2px; }
  .result-column li::before { content: "›"; margin-right: 8px; color: var(--neutral-grey); }
  .result-for { left: 39px; height: 190px; background: var(--for-bg); clip-path: polygon(0 0,100% 0,100% 89%,50% 100%,0 89%); }
  .result-against { left: 254px; height: 162px; background: var(--against-bg); clip-path: polygon(0 0,100% 0,100% 83%,50% 100%,0 83%); }
  .result-abstain { left: 467px; height: 110px; background: var(--abstain-bg); clip-path: polygon(0 0,100% 0,100% 85%,50% 100%,0 85%); }

  .site-footer { position: absolute; top: 707px; left: 0; width: 727px; border-top: 1px solid var(--rule); padding: 18px 0 0 67px; font-size: 9px; color: var(--text-muted); }
</style>
</head>
<body>
  <header class="site-header">
    <div class="brand"><span class="brand-mark"></span><span class="brand-name">Qarvel Engineers</span></div>
    <nav class="main-nav"><a href="#">Home</a><a href="#">Help</a><a href="#">Logout</a></nav>
  </header>

  <section class="motion-band">
    <h1 class="motion-title">Current Motion # : 541</h1>
    <p class="motion-desc">Write any description about current motion.</p>
  </section>

  <h2 class="section-title speak-title">I would like to Speak :</h2>
  <div class="speak-options">
    <div class="speak-option">
      <svg viewBox="0 0 44 44"><circle cx="22" cy="22" r="21" fill="#dfeff7" stroke="var(--brand-blue)" stroke-width="2"/><circle cx="22" cy="22" r="16" fill="var(--tick-green)"/><path d="M14 22l6 6 11-12" fill="none" stroke="#fff" stroke-width="4" stroke-linecap="round" stroke-linejoin="round"/></svg>
      <div><div class="option-label is-active">For Motion</div><div class="option-sub">Subhead goes here</div></div>
    </div>
    <div class="speak-option">
      <svg viewBox="0 0 44 44"><circle cx="22" cy="22" r="21" fill="#eee" stroke="#bbb" stroke-width="2"/><circle cx="22" cy="22" r="16" fill="var(--cross-red)"/><path d="M16 16l12 12M28 16l-12 12" stroke="#fff" stroke-width="4" stroke-linecap="round"/></svg>
      <div><div class="option-label">Against Motion</div><div class="option-sub">Subhead goes here</div></div>
    </div>
    <div class="speak-option">
      <svg viewBox="0 0 44 44"><circle cx="22" cy="22" r="21" fill="#eee" stroke="#bbb" stroke-width="2"/><circle cx="22" cy="22" r="16" fill="var(--neutral-grey)"/><path d="M22 13v12" stroke="#fff" stroke-width="4" stroke-linecap="round"/><circle cx="22" cy="31" r="2.4" fill="#fff"/></svg>
      <div><div class="option-label">Remove From Queue</div><div class="option-sub">Subhead goes here</div></div>
    </div>
  </div>

  <h2 class="section-title results-title">Voting Results :</h2>
  <div class="result-column result-for">
    <h3>For</h3>
    <ul><li>A. Marsh</li><li>D. Pellow</li><li>L. Terrin</li><li>SA. Venn</li><li>P. Lindqvist</li><li>B. Holt</li><li>R. Okafor</li><li>S. Brame</li></ul>
  </div>
  <div class="result-column result-against">
    <h3>Against</h3>
    <ul><li>P. Lindqvist</li><li>B. Holt</li><li>R. Okafor</li><li>S. Brame</li><li>A. Marsh</li><li>D. Pellow</li></ul>
  </div>
  <div class="result-column result-abstain">
    <h3>Abstain</h3>
    <ul><li>S. Brame</li><li>A. Marsh</li><li>D. Pellow</li><li>L. Terrin</li></ul>
  </div>

  <footer class="site-footer">Copyright 2012 Qarvel Engineers &nbsp;|&nbsp; All Rights Reserved &nbsp;|&nbsp; webmaster</footer>
</body>
</html>
```